Verdant Orchard - Stationery Design Project

We need a stationary for our business. We grow roots and fruits in Central and South America, we import and distribute in FL, USA. We do fresh and frozen products.

Target Market(s)

Small and big supermarkets, wholesalers, traders, distributors, etc

Industry/Entity Type

Business

```html
<!DOCTYPE html>
<html lang="en">
<head>
<meta charset="utf-8">
<title>Verdant Orchard – Envelope</title>
<link rel="stylesheet" href="https://fonts.googleapis.com/css2?family=Montserrat:wght@500&display=swap">
<style>
  :root {
    --paper: #ffffff;
    --canvas: #ffffff;
    --edge: #6f6f6f;
    --orange: #ff6a00;
    --leaf-green: #3f5f1c;
    --window-edge: #7a7a7a;
  }
  html, body {
    margin: 0;
    padding: 0;
    width: 1200px;
    height: 758px;
    overflow: hidden;
    background: var(--canvas);
  }
  .stage {
    position: relative;
    width: 1200px;
    height: 758px;
  }
  .envelope-back {
    position: absolute;
    left: 0;
    top: 0;
    width: 1200px;
    height: 758px;
  }
  .envelope-front {
    position: absolute;
    left: 39px;
    top: 117px;
    width: 948px;
    height: 598px;
    background: var(--paper);
    border: 1px solid var(--edge);
    box-sizing: border-box;
    overflow: hidden;
  }
  .side-band {
    position: absolute;
    right: 0;
    top: 0;
    width: 50px;
    height: 100%;
    background: var(--orange);
  }
  .base-stripe {
    position: absolute;
    left: 0;
    bottom: 0;
    width: 470px;
    height: 7px;
    background: linear-gradient(90deg, var(--orange) 0%, rgba(255,106,0,0.55) 55%, rgba(255,106,0,0) 100%);
  }
  .brand-name {
    position: absolute;
    left: 58px;
    top: 72px;
    margin: 0;
    font-family: "Montserrat", sans-serif;
    font-weight: 500;
    font-size: 38px;
    letter-spacing: 0.5px;
    color: var(--leaf-green);
    white-space: nowrap;
  }
  .address-window {
    position: absolute;
    left: 86px;
    top: 199px;
    width: 241px;
    height: 127px;
    border: 1px solid var(--window-edge);
    border-radius: 22px;
    box-sizing: border-box;
  }
  .orchard-tree {
    position: absolute;
    left: 0;
    top: 395px;
    width: 116px;
    height: 196px;
    background: radial-gradient(ellipse at 55% 35%, #8fe35a 0%, #b8ef8e 45%, rgba(255,255,255,0) 75%),
                linear-gradient(180deg, rgba(255,255,255,0) 50%, #8a5a5e 100%);
    border-radius: 0 60px 0 0;
    opacity: 0.85;
  }
</style>
</head>
<body>
  <main class="stage">
    <svg class="envelope-back" viewBox="0 0 1200 758" aria-hidden="true">
      <rect x="213.5" y="40.5" width="946" height="599" fill="#ffffff" stroke="#6f6f6f" stroke-width="1"/>
      <path d="M214 44 Q 222 62 248 62 L 1085 62" fill="none" stroke="#6f6f6f" stroke-width="1"/>
      <path d="M1160 40 L 1126 40 Q 1085 40 1085 82 L 1085 598 Q 1085 640 1126 640 L 1160 640 Z" fill="#ff6a00"/>
    </svg>

    <section class="envelope-front">
      <h1 class="brand-name">Verdant Orchard</h1>
      <div class="address-window"></div>
      <div class="orchard-tree" role="img" aria-label="Illustration of a fruit tree with green leaves and red fruit"></div>
      <div class="base-stripe"></div>
      <div class="side-band"></div>
    </section>
  </main>
</body>
</html>
```